Ledgerwise Systems Group business card design.

We are a software development company that develop Software for finance companies and related industries.

We need a 2 sided business card designed. We have a new logo already designed (see attached eps and ai) We are after a clean simple corporate look. One side with just our logo, and the second side with our details.

Mark Hollister
Managing Director

Suite 4 Level 9, 138 Kellaway Street Sydney NSW 2000

Direct: +61 2 9374 6021
Mobile: +61 4 2287 5196
Email: markh@lsg-example.net.au
Web: www.lsg-example.net.au

I have included 2 logo files an .ai and .eps. I noticed that the lines either side of the group looks a bit jaggered and needs to be made sharper.

I would like to introduce a little colour somewhere rather than having it all black and white. But not over the top, keeping with a simple clean corporate look. Perhaps a light blue on some of the text?

If you have other ideas would be pleased to review

Regards

Mark H.

```html
<!DOCTYPE html>
<html lang="en">
<head>
<meta charset="utf-8">
<title>Ledgerwise Systems Group – Business Card</title>
<link href="https://fonts.googleapis.com/css2?family=Open+Sans:wght@400;600;700&display=swap" rel="stylesheet">
<style>
  :root {
    --backdrop: #e7e4df;
    --card-black: #0b0b0c;
    --card-white: #fbfbfa;
    --ink: #111112;
    --ink-soft: #4a4a4d;
    --accent-blue: #7cc2ea;
    --white: #ffffff;
    --rule-grey: #8a8a8e;
  }
  * { margin: 0; padding: 0; box-sizing: border-box; }
  html, body {
    width: 1200px;
    height: 913px;
    overflow: hidden;
    background: var(--backdrop);
    font-family: "Open Sans", Arial, sans-serif;
  }
  .stage { position: relative; width: 1200px; height: 913px; }

  .card {
    position: absolute;
    width: 500px;
    height: 306px;
    border-radius: 4px;
    box-shadow: 0 6px 18px rgba(0,0,0,0.18);
  }

  /* Front: logo side */
  .card--front {
    left: 90px;
    top: 150px;
    background: var(--card-black);
    display: flex;
    flex-direction: column;
    align-items: center;
    justify-content: center;
  }
  .brand-mark {
    width: 54px;
    height: 54px;
    background: var(--white);
    margin-bottom: 22px;
  }
  .brand-name {
    color: var(--white);
    font-weight: 700;
    font-size: 24px;
    letter-spacing: 1px;
    text-transform: uppercase;
  }
  .brand-rule {
    width: 330px;
    height: 1px;
    background: var(--rule-grey);
    margin-top: 14px;
  }

  /* Back: details side */
  .card--back {
    left: 610px;
    top: 430px;
    background: var(--card-white);
  }
  .back-brand {
    position: absolute;
    left: 48px;
    top: 78px;
    display: flex;
    flex-direction: column;
    align-items: center;
  }
  .back-brand__mark {
    width: 120px;
    height: 120px;
    background: var(--ink);
  }
  .back-brand__name {
    margin-top: 12px;
    color: var(--ink);
    font-weight: 700;
    font-size: 14px;
  }

  .details {
    position: absolute;
    left: 250px;
    top: 44px;
    width: 230px;
    color: var(--ink-soft);
  }
  .details__name {
    color: var(--accent-blue);
    font-weight: 600;
    font-size: 17px;
    line-height: 1.1;
  }
  .details__title {
    font-size: 11px;
    margin-top: 2px;
  }
  .details__address {
    font-size: 12px;
    line-height: 1.45;
    margin-top: 26px;
  }
  .contact-list {
    list-style: none;
    margin-top: 16px;
    font-size: 12px;
    line-height: 1.55;
    color: var(--ink);
  }
  .contact-list li {
    display: flex;
    align-items: center;
    gap: 9px;
  }
  .contact-icon {
    width: 11px;
    height: 11px;
    flex: none;
  }
</style>
</head>
<body>
  <main class="stage">

    <section class="card card--front" aria-label="Business card front">
      <div class="brand-mark"></div>
      <div class="brand-name">Ledgerwise Systems Group</div>
      <div class="brand-rule"></div>
    </section>

    <section class="card card--back" aria-label="Business card back">
      <div class="back-brand">
        <div class="back-brand__mark"></div>
        <div class="back-brand__name">Ledgerwise</div>
      </div>

      <div class="details">
        <p class="details__name">Mark Hollister</p>
        <p class="details__title">Managing Director</p>

        <p class="details__address">Suite 4 Level 9, 138 Kellaway Street<br>Sydney NSW 2000</p>

        <ul class="contact-list">
          <li>
            <svg class="contact-icon" viewBox="0 0 12 12" aria-hidden="true"><path fill="#7cc2ea" d="M1 3.5C1 2.5 2 2 6 2s5 .5 5 1.5V5H8.5V4h-5v1H1zM2.5 6h7l1 4h-9z"/></svg>
            +61 2 9374 6021
          </li>
          <li>
            <svg class="contact-icon" viewBox="0 0 12 12" aria-hidden="true"><rect x="3" y="0.5" width="6" height="11" rx="1" fill="#7cc2ea"/><rect x="4" y="2" width="4" height="7" fill="#fff"/></svg>
            +61 4 2287 5196
          </li>
          <li>
            <svg class="contact-icon" viewBox="0 0 12 12" aria-hidden="true"><rect x="0.5" y="2.5" width="11" height="7" fill="#7cc2ea"/><path d="M1 3l5 3.5L11 3" stroke="#fff" fill="none"/></svg>
            markh@lsg-example.net.au
          </li>
          <li>
            <svg class="contact-icon" viewBox="0 0 12 12" aria-hidden="true"><circle cx="6" cy="6" r="5.2" fill="#7cc2ea"/><path d="M1 6h10M6 1c-2.5 3-2.5 7 0 10M6 1c2.5 3 2.5 7 0 10" stroke="#fff" stroke-width=".8" fill="none"/></svg>
            www.lsg-example.net.au
          </li>
        </ul>
      </div>
    </section>

  </main>
</body>
</html>
```